Starter & Alternator business needs a website

update: very good designs submitted so far. also need this to display well on mobile devices. not sure if wordpress or html/css is better for my needs.

Our existing website is vellumtorq.com and is need of total revamp. Need full design of a website for my business.

We sell and rebuild starters and alternators. Customers bring in the units and we rebuild them. Or we sell them brand new or rebuilt units we have in stock. We do not install units into vehicles like a mechanic would. We strictly rebuild starters and alternators in our shop, sell brand new units over the counter, and we do deliver occasionally as well. We do offer a line of Orvan batteries as well but that is only a small feature of the business.

I would like this website designed and coded. I can upload the files to my web host after completion. I can also add in and modify content like our background info, etc.

I have included an illustrator file that shows some of our signage and logo, etc. I have also included a radio commercial sample so you can get a little better feel for the business. A similar ad does run on the radio currently, slightly different and without the added sound effects.

Update: I do like using photos of real items(starters or alternators etc) for an icon, like a real alternator stock image for the alternator section icon, etc. Maybe incorporate our logo in that design as well. That looks nice as well and may aid in navigation.

For any other design elements, do what you think looks good. Our colors are red/white/blue as seen in the illustrator file. our building is painted with halbeck moray colors, ember gala red and deep tide for blue.

Here are some examples of rebuilders websites in other markets for reference:

https://quillmarauto.com/starter-alternator-rebuilding/

https://www.dunwickmotorworks.com/auto-repairs/alternator-starter-rebuilds.aspx

https://www.fjordvoltage.com/

https://www.pemberlowgx.com/

The website can have areas for: services and products offered, high output alternators, Orvan Batteries, troubleshooting tips, current specials, contact info and directions/map, etc. Whatever else you feel applies.

At some point I do want to be able to sell items directly online or at least have a secure section for customers to submit invoice payments, but that's not necessarily in scope for this project just something to keep in mind.

Target Market(s)

Mechanics and Managers in fleet shops, construction and marine industries, shipping trades. Also automobile owners who work on their own vehicles. We sell and rebuild starters and alternators for automobiles, heavy duty equipment, forklifts, traxlifts, man movers, ferrettes, loaders, large tractors and trucks, just about any engine, golf carts, generators, etc.

Industry/Entity Type

Automotive Part

Coding

Coded - Design and coding required

Number of Pages Required

5+ page

Font styles to use
Serif
Sans Serif

Colors
0255a3
ec1f27
ffffff

Requirements
Must have
• Should also display nicely on mobile phones. Highlight our specialty, "Starters & Alternators"

```html
<!DOCTYPE html>
<html lang="en">
<head>
<meta charset="utf-8">
<title>Vellumtorq Rebuilders Oahu — Starters &amp; Alternators</title>
<link rel="stylesheet" href="https://fonts.googleapis.com/css2?family=Arimo:wght@400;700&family=Crimson+Pro:wght@600&family=Playfair+Display+SC:wght@700&display=swap">
<style>
  :root {
    --brand-blue: #3a4fa8;
    --brand-red: #ec1f27;
    --ink: #111111;
    --white: #ffffff;
    --night: #000000;
    --sky: #1b2744;
    --wall: #6e1212;
    --trim: #10276b;
  }
  * { box-sizing: border-box; margin: 0; padding: 0; }
  html, body { width: 1200px; height: 800px; overflow: hidden; background: var(--white); }
  body { font-family: "Arimo", Arial, sans-serif; color: var(--ink); }

  .site { width: 1200px; height: 800px; position: relative; }

  .hero {
    position: relative;
    height: 440px;
    background: var(--night);
    overflow: hidden;
  }
  .hero__photo {
    position: absolute; inset: 0 0 90px 0;
    background: linear-gradient(180deg, var(--sky) 0%, #2a1a2e 28%, var(--wall) 48%, #4a0c10 62%, var(--trim) 72%, #0c0f1c 86%, var(--night) 100%);
  }
  .hero__fade {
    position: absolute; left: 0; right: 0; bottom: 0; height: 260px;
    background: linear-gradient(180deg, rgba(0,0,0,0) 0%, rgba(0,0,0,0.75) 45%, var(--night) 70%);
  }

  .nav {
    position: absolute; top: 36px; right: 48px;
    display: flex; gap: 10px; align-items: center;
    list-style: none;
  }
  .nav__link {
    display: block;
    padding: 11px 20px;
    color: var(--white);
    text-decoration: none;
    font-weight: 700;
    font-size: 14px;
    letter-spacing: 3px;
    border: 2px solid transparent;
    border-radius: 8px;
  }
  .nav__link--active { border-color: var(--white); }

  .hero__titles {
    position: absolute; left: 0; right: 0; top: 285px;
    text-align: center;
  }
  .hero__company {
    font-family: "Crimson Pro", Georgia, serif;
    font-weight: 600;
    font-size: 34px;
    letter-spacing: 2px;
    color: var(--brand-blue);
  }
  .hero__specialty {
    font-family: "Playfair Display SC", Georgia, serif;
    font-weight: 700;
    font-size: 56px;
    line-height: 1.05;
    letter-spacing: 2px;
    color: var(--brand-red);
  }

  .services { padding-top: 38px; text-align: center; }
  .services__heading {
    font-size: 40px; font-weight: 700;
    color: var(--brand-blue);
  }
  .services__intro { margin-top: 14px; font-size: 17px; }

  .services__list {
    list-style: none;
    display: flex; justify-content: center; gap: 78px;
    margin-top: 34px;
  }
  .service { width: 240px; }
  .service__photo { height: 180px; }
  .service__photo--marine { background: linear-gradient(180deg, #8fb4e4 0%, #cfdff2 40%, #4a5a3c 70%, #2e3626 100%); }
  .service__photo--heavy { background: linear-gradient(180deg, #3b3b3b 0%, #6b5a32 45%, #c9a02a 65%, #4a4538 100%); }
  .service__photo--auto { background: linear-gradient(180deg, #c8531f 0%, #9aa0a8 45%, #d8dadd 70%, #6c7076 100%); }
  .service__caption { margin-top: 14px; font-size: 16px; }
  .service__caption--left { text-align: left; padding-left: 4px; }
  .service__caption--mid { text-align: left; padding-left: 14px; }
</style>
</head>
<body>
<div class="site">
  <header class="hero">
    <div class="hero__photo" role="img" aria-label="Photo of the red and blue shop building against an evening sky"></div>
    <div class="hero__fade"></div>
    <nav>
      <ul class="nav">
        <li><a class="nav__link nav__link--active" href="#">HOME</a></li>
        <li><a class="nav__link" href="#">SERVICES</a></li>
        <li><a class="nav__link" href="#">ABOUT</a></li>
        <li><a class="nav__link" href="#">CONTACT</a></li>
      </ul>
    </nav>
    <div class="hero__titles">
      <p class="hero__company">Vellumtorq Rebuilders Oahu</p>
      <h1 class="hero__specialty">Starters &amp; Alternators</h1>
    </div>
  </header>

  <section class="services">
    <h2 class="services__heading">Our Services</h2>
    <p class="services__intro">Your source for New and High-Quality Rebuilt Starters &amp; Alternators.</p>
    <ul class="services__list">
      <li class="service">
        <div class="service__photo service__photo--marine" role="img" aria-label="Photo of service members looking out over a harbor"></div>
        <p class="service__caption service__caption--left">Serving the Marine</p>
      </li>
      <li class="service">
        <div class="service__photo service__photo--heavy" role="img" aria-label="Photo of a yellow excavator loading a mining truck"></div>
        <p class="service__caption service__caption--mid">Heavy Duty</p>
      </li>
      <li class="service">
        <div class="service__photo service__photo--auto" role="img" aria-label="Photo of robotic arms on a car assembly line"></div>
        <p class="service__caption">Automotive industries</p>
      </li>
    </ul>
  </section>
</div>
</body>
</html>
```